Etiketten-Design für Honiggläser
Zielgruppe
Imkerei Lindner
Wir sind eine Familienbetrieb und vertreiben hochwertigen Honig aus eigener Imkerei
Aufgabenstellung
Es werden Etiketten für Honiggläser benötigt
Es gibt drei verschiedene Größen von Gläser (siehe Anhang) und je größe einmal „Frühtracht“ und einmal „Sommertracht“
Also insgesamt 6 Etiketten
500g Frühtracht und Sommertracht
250g Frühtracht und Sommertracht
150g Frühtracht und Sommertracht

```html
<!DOCTYPE html>
<html lang="de">
<head>
<meta charset="utf-8">
<title>Honig Frühtracht – Etikett 500g</title>
<link rel="stylesheet" href="https://fonts.googleapis.com/css2?family=Barlow:wght@400;500&family=Barlow+Condensed:wght@300;500;600&display=swap">
<style>
  :root {
    --page-bg: #f1f1f1;
    --label-bg: #0d0e1c;
    --gold: #e9a24a;
    --gold-glow: rgba(214, 178, 92, 0.16);
    --text-light: #f2f2f2;
    --badge-green: #9bc33b;
    --badge-white: #ffffff;
  }
  html, body {
    margin: 0;
    padding: 0;
    width: 1200px;
    height: 766px;
    overflow: hidden;
    background: var(--page-bg);
  }
  .label {
    position: absolute;
    left: 20px;
    top: 230px;
    width: 1160px;
    height: 305px;
    background: var(--label-bg);
    overflow: hidden;
    font-family: "Barlow", sans-serif;
  }
  .pattern {
    position: absolute;
    background: radial-gradient(closest-side, var(--gold-glow), rgba(214, 178, 92, 0.06) 60%, rgba(214, 178, 92, 0) 100%);
  }
  .pattern--left-bottom { left: -20px; top: 180px; width: 190px; height: 150px; }
  .pattern--center-top { left: 300px; top: -30px; width: 530px; height: 150px; }
  .pattern--center-bottom { left: 280px; top: 180px; width: 540px; height: 150px; }
  .pattern--right-top { left: 1020px; top: -10px; width: 160px; height: 150px; }

  .badge-eu {
    position: absolute;
    left: 77px;
    top: 26px;
    width: 115px;
    height: 76px;
    background: var(--badge-green);
  }
  .control-code {
    position: absolute;
    left: 77px;
    top: 106px;
    width: 115px;
    text-align: center;
    color: var(--text-light);
    font-size: 13px;
  }
  .badge-seal {
    position: absolute;
    left: 84px;
    top: 140px;
    width: 100px;
    height: 96px;
    border-radius: 12px;
    background: var(--badge-white);
  }

  .brand {
    position: absolute;
    left: 0;
    width: 1094px;
    text-align: center;
    color: var(--gold);
    margin: 0;
  }
  .brand__name {
    top: 36px;
    font-family: "Barlow Condensed", sans-serif;
    font-weight: 500;
    font-size: 38px;
    letter-spacing: 1px;
    line-height: 1;
  }
  .product__title {
    top: 96px;
    font-family: "Barlow Condensed", sans-serif;
    font-weight: 600;
    font-size: 58px;
    line-height: 1;
  }
  .product__variety {
    top: 152px;
    font-family: "Barlow Condensed", sans-serif;
    font-weight: 300;
    font-size: 50px;
    letter-spacing: 1px;
    line-height: 1;
  }
  .product__weight {
    top: 273px;
    font-family: "Barlow Condensed", sans-serif;
    font-weight: 600;
    font-size: 20px;
    line-height: 1;
  }

  .info {
    position: absolute;
    left: 898px;
    top: 33px;
    color: var(--text-light);
    font-size: 15px;
    line-height: 16px;
    letter-spacing: 0.3px;
  }
  .info p { margin: 0 0 16px; }
  .best-before {
    position: absolute;
    left: 898px;
    top: 217px;
    width: 186px;
    height: 35px;
    background: var(--badge-white);
  }
  .origin {
    position: absolute;
    left: 898px;
    top: 258px;
    color: var(--text-light);
    font-size: 15px;
    line-height: 16px;
    letter-spacing: 0.3px;
    margin: 0;
  }
</style>
</head>
<body>
  <main class="label">
    <div class="pattern pattern--left-bottom" role="img" aria-label="Goldenes Wabenmuster"></div>
    <div class="pattern pattern--center-top" role="img" aria-label="Goldenes Wabenmuster"></div>
    <div class="pattern pattern--center-bottom" role="img" aria-label="Goldenes Wabenmuster"></div>
    <div class="pattern pattern--right-top" role="img" aria-label="Goldenes Wabenmuster"></div>

    <div class="badge-eu" role="img" aria-label="Bio-Siegel der EU"></div>
    <div class="control-code">AT-BIO-xxx</div>
    <div class="badge-seal" role="img" aria-label="Staatliches Bio-Siegel"></div>

    <p class="brand brand__name">Imkerei Lindner</p>
    <h1 class="brand product__title">Honig</h1>
    <p class="brand product__variety">Frühtracht</p>
    <p class="brand product__weight">500g</p>

    <div class="info">
      <p>Imkerei Lindner</p>
      <p>Lindenweg 4,<br>31712 Wiesental<br>Info@imkereilindner.de<br>www.imkereilindner.de</p>
      <p>Nettofüllmenge: 500g<br>Lagerbedingungen,<br>- dunkel, kühl und trocken<br>Mindesthaltbarkeitsdatum,</p>
    </div>
    <div class="best-before"></div>
    <p class="origin">Deutscher Honig aus eigener Imkerei</p>
  </main>
</body>
</html>
```